Web design for financial services

A modern web design of financial services (brokerage firm)
Req.s and technology tags :
- Very mobile friendly.
- One paged with some inner pages.
- Animated sticky header .
- Member login area for e-trade.
- Support RTL language.
- HTML & CSS.

The logo will be Home link
• ORNY :
WHO WE ARE
Content :
i) Board of Directors
ii) Mission Statement
iii) Corporate Values
iv) Regulations
• Financial Services :
WHAT WE DO
Content:
i) Electronic trading
ii) Trading desk
iii) Institutional
iv) Investors Education
• News
• Market Tools
• Forms---- opens new page
• Careers---- opens new page
• Contact Us----opens new page

The website is :
http://www.orny-halvet.com/

The logo need some changes to be more modern and impressively , but with keeping same structure .

Some related websites :
https://www.vexdalo.com.qa/

financial market

Financial Service

2 page

• same fonts of http://www.tuwmallow.com/

• - Very mobile friendly.
• - One paged with some inner pages.
• - Animated sticky header .
• - Member login area for e-trade.
• - Support RTL language.
• - HTML & CSS.
• Slider , some Qatari theme,
• i like the video inside the home page
• ex :http://www.tuwmallow.com/

```html
<!DOCTYPE html>
<html lang="en">
<head>
<meta charset="utf-8">
<title>ORNY Financial Services</title>
<link href="https://fonts.googleapis.com/css2?family=Cinzel:wght@400;700&family=Roboto:wght@400;500;700&display=swap" rel="stylesheet">
<style>
:root{
  --red:#a3100f;
  --red-dark:#8a0c0b;
  --black:#0e0e0e;
  --ink:#222;
  --grey:#666;
  --light:#f4f4f4;
  --contact:#4b4b4b;
  --white:#fff;
}
*{box-sizing:border-box;margin:0;padding:0}
html,body{width:1200px;height:3879px;overflow:hidden}
body{font-family:'Roboto',Arial,sans-serif;color:var(--ink);background:var(--white);position:relative}
section,header,nav,footer,div,a,span,p,h1,h2,h3{position:absolute}
a{text-decoration:none;color:inherit}
.serif{font-family:'Cinzel',Georgia,serif}

/* top bar */
.topbar{left:0;top:0;width:1200px;height:41px;background:var(--black);color:var(--white);font-size:13px}
.topbar .support{left:78px;top:12px;display:flex;align-items:center;gap:7px}
.topbar .login{left:922px;top:12px;display:flex;align-items:center;gap:6px}
.topbar .lang{left:1015px;top:12px;display:flex;align-items:center;gap:6px}
.flag{position:static;display:inline-block;width:20px;height:12px;background:#3b4f8c;border:1px solid #ccc}

/* nav */
.nav{left:0;top:41px;width:1200px;height:130px;background:var(--white)}
.brand{left:78px;top:44px;display:flex;align-items:center;gap:10px}
.brand .mark{position:static;width:34px;height:34px;border-radius:50%;background:var(--red)}
.brand .name{position:static;font-size:32px;font-weight:700;color:var(--red)}
.menu{left:323px;top:47px;display:flex;align-items:center;font-size:19px;color:var(--ink)}
.menu a{position:static;margin-right:32px}
.menu .active{background:var(--red);color:var(--white);padding:9px 28px;border-radius:22px;margin-right:30px}

/* hero */
.hero{left:0;top:171px;width:1200px;height:571px;background:linear-gradient(100deg,#6d8290 0%,#c5d2da 35%,#eef2f4 55%,#a7b6bf 80%,#d9e1e6 100%)}
.hero .title{left:80px;top:160px;font-size:98px;font-weight:700;color:var(--red);line-height:1}
.hero .sub{left:80px;top:262px;font-size:50px;font-weight:700;color:#151515;letter-spacing:1px}
.hero .cta{left:80px;top:338px;width:207px;height:55px;background:var(--red);color:var(--white);font-family:'Cinzel',Georgia,serif;font-size:18px;font-weight:700;display:flex;align-items:center;justify-content:center}

.section-title{left:0;width:1200px;text-align:center;font-family:'Cinzel',Georgia,serif;font-weight:700;font-size:38px}

.arrow{width:30px;height:30px;display:flex;align-items:center;justify-content:center;color:var(--white)}
.arrow.red{background:var(--red)}
.arrow.dark{background:var(--black)}

/* who we are */
.who{left:0;top:742px;width:1200px;height:520px;background:var(--white)}
.who .section-title{top:45px}
.who .card{top:122px;width:250px}
.who .card .photo{position:static;display:block;width:250px;height:166px}
.who .card h3{position:static;margin-top:22px;text-align:center;color:var(--red);font-size:18px;font-weight:400}
.who .card p{position:static;margin-top:12px;text-align:center;color:var(--grey);font-size:12px;line-height:1.4}
.who .more{left:520px;top:426px;width:160px;height:40px;background:var(--red);color:var(--white);font-family:'Cinzel',Georgia,serif;font-weight:700;font-size:16px;display:flex;align-items:center;justify-content:center}

/* services */
.services{left:0;top:1262px;width:1200px;height:781px;color:var(--white)}
.services .backdrop{left:0;top:0;width:1200px;height:781px;background:radial-gradient(circle at 55% 45%,#5a5a5a 0%,#2c2c2c 45%,#141414 100%)}
.services .section-title{top:48px;color:var(--white)}
.services .hub{left:524px;top:262px;width:124px;height:124px;border-radius:50%;background:var(--white);display:flex;align-items:center;justify-content:center;font-weight:700;font-size:26px;color:var(--red)}
.services .lines{left:0;top:0}
.service{width:330px;text-align:center}
.service .icon{position:static;display:block;margin:0 auto;height:130px;border-radius:8px}
.service h3{position:static;margin-top:18px;font-size:20px;font-weight:700}
.service p{position:static;margin-top:12px;font-size:12.5px;line-height:1.5;color:#e6e6e6}

/* news */
.news{left:0;top:2043px;width:1200px;height:491px;background:var(--light)}
.news .section-title{top:45px}
.news .card{top:125px;width:332px}
.news .card .photo{position:relative;display:block;width:332px;height:187px}
.news .badge{left:0;top:0;width:52px;height:58px;color:var(--white);text-align:center;padding-top:4px}
.news .badge b{display:block;font-size:28px;font-weight:500;line-height:1.1}
.news .badge i{display:block;font-style:normal;font-size:12px}
.news .card h3{position:static;margin-top:22px;font-size:18px;font-weight:400;color:var(--ink)}
.news .card p{position:static;margin-top:12px;font-size:13px;line-height:1.55;color:var(--grey)}
.news .card .read{position:static;display:block;margin-top:16px;font-size:14px;color:var(--ink)}

/* market tools */
.tools{left:0;top:2534px;width:1200px;height:574px;background:linear-gradient(120deg,#a8454b 0%,#c66a70 50%,#b5525a 100%)}
.tools .section-title{top:45px;color:var(--white)}
.tool{top:131px;width:332px;height:375px;background:var(--white)}
.tool .photo{left:0;top:0;width:332px;height:260px}
.tool .caption{left:28px;top:278px;width:280px}
.tool .caption small{display:block;font-size:13px;color:var(--grey)}
.tool .caption strong{display:block;margin-top:6px;font-size:18px;font-weight:500;line-height:1.35;color:var(--ink)}
.tool.text .inner{left:28px;top:32px;width:280px}
.tool.text .kicker{position:static;font-size:13px;color:var(--grey);letter-spacing:.5px}
.tool.text h3{position:static;margin-top:14px;font-size:21px;font-weight:500;line-height:1.35}
.tool.text p{position:static;margin-top:16px;font-size:13px;line-height:1.6;color:var(--grey)}
.tool.text .rule{position:static;margin-top:28px;width:48px;border-top:1px solid #999}

/* newsletter */
.newsletter{left:0;top:3108px;width:1200px;height:187px;background:var(--black);color:var(--white)}
.newsletter h2{left:80px;top:50px;font-family:'Cinzel',Georgia,serif;font-weight:700;font-size:42px}
.newsletter p{left:80px;top:115px;font-size:15px}
.newsletter .field{left:590px;top:67px;width:365px;height:53px;background:var(--white);color:#777;font-size:14px;padding:18px 16px}
.newsletter .btn{left:965px;top:67px;width:158px;height:53px;background:var(--red);font-family:'Cinzel',Georgia,serif;font-weight:700;font-size:18px;display:flex;align-items:center;justify-content:center}

/* contact */
.contact{left:0;top:3295px;width:1200px;height:532px;background:var(--contact);color:var(--white)}
.contact .section-title{top:48px;color:var(--white);font-size:38px}
.contact .intro{left:270px;top:103px;width:660px;text-align:center;font-size:15px;line-height:1.65}
.contact .input{height:52px;background:var(--white);color:#555;font-size:13px;padding:18px 18px}
.contact .submit{left:580px;top:373px;width:155px;height:50px;border:1px solid #ddd;font-size:15px;display:flex;align-items:center;justify-content:center;letter-spacing:.5px}
.contact .info{left:820px;top:180px;width:300px}
.contact .info h3{position:static;font-family:'Cinzel',Georgia,serif;font-weight:700;font-size:19px}
.contact .row{position:relative;display:flex;align-items:flex-start;gap:24px;margin-top:24px;font-size:14px;line-height:1.6}
.contact .row svg{flex:none}
.contact .social{left:820px;top:435px;display:flex;gap:22px}
.contact .social span{position:static;width:48px;height:48px;border:1px solid #ccc}
.contact .social span.first{background:#d63b3b;border-color:#d63b3b}

.footer{left:0;top:3827px;width:1200px;height:52px;background:var(--contact);color:var(--white);font-size:13px;text-align:center;padding-top:17px}
.footer::before{content:"";position:absolute;left:78px;right:78px;top:0;border-top:1px solid #777}
</style>
</head>
<body>

<header class="topbar">
  <span class="support">
    <svg width="14" height="14" viewBox="0 0 14 14"><circle cx="7" cy="7" r="6" fill="none" stroke="#fff" stroke-width="1.5"/><path d="M7 3v4l3 2" stroke="#fff" stroke-width="1.5" fill="none"/></svg>
    24/7 Support : (123)4567890
  </span>
  <a class="login" href="#">
    <svg width="12" height="14" viewBox="0 0 12 14"><rect x="1" y="6" width="10" height="8" fill="#fff"/><path d="M3 6V4a3 3 0 0 1 6 0v2" stroke="#fff" stroke-width="1.6" fill="none"/></svg>
    Login
  </a>
  <span class="lang"><span class="flag"></span> English
    <svg width="10" height="6" viewBox="0 0 10 6"><path d="M0 0h10L5 6z" fill="#fff"/></svg>
  </span>
</header>

<nav class="nav">
  <a class="brand" href="#"><span class="mark"></span><span class="name">ORNY</span></a>
  <div class="menu">
    <a class="active" href="#">Home</a>
    <a href="#">ORNY</a>
    <a href="#">Financial Service</a>
    <a href="#">News</a>
    <a href="#">Market Tools</a>
    <a href="#">Forms</a>
    <a href="#">Careers</a>
  </div>
</nav>

<section class="hero" role="img" aria-label="Business people walking past a glass office tower">
  <h1 class="title">ORNY</h1>
  <p class="sub serif">FINANCIAL SERVICES</p>
  <a class="cta" href="#">JOIN US NOW</a>
</section>

<section class="who">
  <h2 class="section-title">Who we are</h2>
  <span class="arrow red" style="left:30px;top:183px"><svg width="10" height="12" viewBox="0 0 10 12"><path d="M8 0L0 6l8 6z" fill="#fff"/></svg></span>
  <span class="arrow dark" style="left:1143px;top:183px"><svg width="10" height="12" viewBox="0 0 10 12"><path d="M2 0l8 6-8 6z" fill="#fff"/></svg></span>

  <div class="card" style="left:78px">
    <span class="photo" role="img" aria-label="Board members around a meeting table" style="background:linear-gradient(135deg,#6f6f6f,#3e3e3e)"></span>
    <h3>Board of Directors</h3>
    <p>Lorem Ipsum is simply dummy text<br>of the printing and typesetting</p>
  </div>
  <div class="card" style="left:345px">
    <span class="photo" role="img" aria-label="Colleagues reviewing a document in an office" style="background:linear-gradient(135deg,#eef1f4,#b8c3cc)"></span>
    <h3>Mission Statement</h3>
    <p>Lorem Ipsum is simply dummy text<br>of the printing and typesetting</p>
  </div>
  <div class="card" style="left:608px">
    <span class="photo" role="img" aria-label="Team discussing notes on a whiteboard" style="background:linear-gradient(135deg,#e6e2dc,#a59a8e)"></span>
    <h3>Corporate Values</h3>
    <p>Lorem Ipsum is simply dummy text<br>of the printing and typesetting</p>
  </div>
  <div class="card" style="left:873px">
    <span class="photo" role="img" aria-label="Group meeting around a bright table" style="background:linear-gradient(135deg,#f3ece6,#c99a87)"></span>
    <h3>Regulations</h3>
    <p>Lorem Ipsum is simply dummy text<br>of the printing and typesetting</p>
  </div>
  <a class="more" href="#">READ MORE</a>
</section>

<section class="services">
  <span class="backdrop" role="img" aria-label="Dark city towers with a plane overhead and a hand pointing up at the hub"></span>
  <svg class="lines" width="1200" height="781" viewBox="0 0 1200 781">
    <g stroke="#cfcfcf" stroke-width="1.5" fill="none">
      <path d="M340 170H430L524 300"/>
      <path d="M820 170H740L648 300"/>
      <path d="M340 490H440L530 360"/>
      <path d="M850 490H740L642 360"/>
    </g>
    <g fill="#fff"><circle cx="340" cy="170" r="4"/><circle cx="820" cy="170" r="4"/><circle cx="340" cy="490" r="4"/><circle cx="850" cy="490" r="4"/></g>
  </svg>
  <h2 class="section-title">Our services</h2>
  <div class="hub">ORNY</div>

  <div class="service" style="left:80px;top:140px">
    <span class="icon" role="img" aria-label="Illustration of a rising chart on a monitor" style="width:170px;background:linear-gradient(135deg,#f2f2f2,#4d8fc9)"></span>
    <h3>Electronic trading</h3>
    <p>Lorem Ipsum is simply dummy text of the printing and typesetting industry. Lorem Ipsum has been the industry's standard.</p>
  </div>
  <div class="service" style="left:795px;top:140px">
    <span class="icon" role="img" aria-label="Illustration of a blue bar chart over papers" style="width:180px;background:linear-gradient(135deg,#f4f4f4,#2f6fb7)"></span>
    <h3>Institutional</h3>
    <p>Lorem Ipsum is simply dummy text of the printing and typesetting industry. Lorem Ipsum has been the industry's standard.</p>
  </div>
  <div class="service" style="left:80px;top:440px">
    <span class="icon" role="img" aria-label="Illustration of a colourful bar chart on documents" style="width:170px;background:linear-gradient(135deg,#f1f1f1,#8bc34a 50%,#e05a4e)"></span>
    <h3>Trading desk</h3>
    <p>Lorem Ipsum is simply dummy text of the printing and typesetting industry. Lorem Ipsum has been the industry's standard.</p>
  </div>
  <div class="service" style="left:820px;top:440px">
    <span class="icon" role="img" aria-label="Illustration of a laptop showing charts" style="width:190px;background:linear-gradient(135deg,#e9e9e9,#5d9ad6 60%,#e5a04a)"></span>
    <h3>Investors Education</h3>
    <p>Lorem Ipsum is simply dummy text of the printing and typesetting industry. Lorem Ipsum has been the industry's standard.</p>
  </div>
</section>

<section class="news">
  <h2 class="section-title">Latest News</h2>
  <span class="arrow red" style="left:30px;top:205px"><svg width="10" height="12" viewBox="0 0 10 12"><path d="M8 0L0 6l8 6z" fill="#fff"/></svg></span>
  <span class="arrow dark" style="left:1143px;top:205px"><svg width="10" height="12" viewBox="0 0 10 12"><path d="M2 0l8 6-8 6z" fill="#fff"/></svg></span>

  <div class="card" style="left:78px">
    <span class="photo" role="img" aria-label="Two young people looking at a tablet outdoors" style="background:linear-gradient(135deg,#d8c9a6,#7f8a5a)">
      <span class="badge" style="background:var(--red)"><b>14</b><i>JAN</i></span>
    </span>
    <h3 style="color:var(--red)">Lorem Ipsum is simply text Dummy</h3>
    <p>Lorem Ipsum is simply dummy text of the<br>printing and typesetting industry.</p>
    <a class="read" href="#" style="color:var(--red)">READ MORE &raquo;</a>
  </div>
  <div class="card" style="left:433px">
    <span class="photo" role="img" aria-label="Business people shaking hands" style="background:linear-gradient(135deg,#eceff2,#4b4f57)">
      <span class="badge" style="background:var(--black)"><b>26</b><i>JAN</i></span>
    </span>
    <h3>Lorem Ipsum is simply text Dummy</h3>
    <p>Lorem Ipsum is simply dummy text of the<br>printing and typesetting industry.</p>
    <a class="read" href="#">READ MORE &raquo;</a>
  </div>
  <div class="card" style="left:791px">
    <span class="photo" role="img" aria-label="Open plan office with staff at desks" style="background:linear-gradient(135deg,#f0f2f4,#8f9aa4)">
      <span class="badge" style="background:var(--black)"><b>30</b><i>JAN</i></span>
    </span>
    <h3>Lorem Ipsum is simply text Dummy</h3>
    <p>Lorem Ipsum is simply dummy text of the<br>printing and typesetting industry</p>
    <a class="read" href="#">READ MORE &raquo;</a>
  </div>
</section>

<section class="tools" role="img" aria-label="Red tinted background of a desk with charts">
  <h2 class="section-title">Market Tools</h2>
  <div class="tool text" style="left:78px">
    <div class="inner">
      <p class="kicker">CAREERS</p>
      <h3>Lorem Ipsum is simply dummy text</h3>
      <p>Lorem Ipsum is simply dummy text of the printing and typesetting industry. Lorem Ipsum has been the industry's standard dummy text ever since the 1500s, when an unknown printer took a galley of type and scrambled it to make a type specimen book.</p>
      <p class="rule"></p>
    </div>
  </div>
  <div class="tool" style="left:433px">
    <span class="photo" role="img" aria-label="Two colleagues smiling over paperwork" style="background:linear-gradient(135deg,#f1ede8,#b89a7c)"></span>
    <div class="caption"><small>Lorem Ipsum is simply dummy</small><strong>Lorem Ipsum is simply dummy text</strong></div>
  </div>
  <div class="tool" style="left:791px">
    <span class="photo" role="img" aria-label="Hand writing beside stacks of coins" style="background:linear-gradient(135deg,#f5f5f5,#c9b27a)"></span>
    <div class="caption"><small>Lorem Ipsum is simply dummy</small><strong>Lorem Ipsum is simply dummy text</strong></div>
  </div>
</section>

<section class="newsletter">
  <h2>NEWSLETTER</h2>
  <p>Subscribe to Our Newsletter to Get News &amp; Updates</p>
  <span class="field">Name</span>
  <a class="btn" href="#">SUBSCRIBE</a>
</section>

<section class="contact">
  <h2 class="section-title" style="font-variant:small-caps">Contact us Now</h2>
  <p class="intro">Lorem Ipsum is simply dummy text of the printing and typesetting industry. Lorem Ipsum has been the industry's standard dummy text.</p>
  <span class="input" style="left:78px;top:183px;width:322px">Your Name</span>
  <span class="input" style="left:413px;top:183px;width:322px">Your E-Mail</span>
  <span class="input" style="left:78px;top:245px;width:322px">Address</span>
  <span class="input" style="left:413px;top:245px;width:322px">Your Phone</span>
  <span class="input" style="left:78px;top:307px;width:657px">Message</span>
  <a class="submit" href="#">SUBMIT</a>

  <div class="info">
    <h3 style="font-variant:small-caps">ORNY Financial Service</h3>
    <div class="row">
      <svg width="22" height="28" viewBox="0 0 22 28"><path d="M11 1a9 9 0 0 0-9 9c0 7 9 16 9 16s9-9 9-16a9 9 0 0 0-9-9z" fill="none" stroke="#fff" stroke-width="1.5"/><circle cx="11" cy="10" r="3" fill="none" stroke="#fff" stroke-width="1.5"/></svg>
      <span style="position:static">Lorem Ipsum is simply dummy text<br>of the printing</span>
    </div>
    <div class="row" style="margin-top:26px">
      <svg width="22" height="22" viewBox="0 0 22 22"><path d="M5 2l4 4-2 3c1 3 3 5 6 6l3-2 4 4-3 3C9 20 2 13 2 5z" fill="none" stroke="#fff" stroke-width="1.5"/></svg>
      <span style="position:static">+974-4000210</span>
    </div>
    <div class="row" style="margin-top:26px">
      <svg width="22" height="16" viewBox="0 0 22 16"><rect x="1" y="1" width="20" height="14" fill="none" stroke="#fff" stroke-width="1.5"/><path d="M1 1l10 8 10-8" fill="none" stroke="#fff" stroke-width="1.5"/></svg>
      <span style="position:static">complaints@orny-halvet.com</span>
    </div>
  </div>
  <div class="social"><span class="first"></span><span></span><span></span></div>
</section>

<footer class="footer">&copy; ORNY Financial service - 2017. All Rights Reserved</footer>

</body>
</html>
```